Zerovan Medical

We are a medical supplier company we sell machines and equipment to all medical sectors in Iraq. Our services include not only the installation of these machines and equipment but also we provide support after installation and we train the staff to use these machines/equipment
We need a website that will make us stand out from our competitors, something professional and catchy
Starting from the home page, before showing the home page we want the loading screen to have our logo animated in a nice way
Then we can proceed to creating the other pages which are
Projects
Services
Training
About
and Contact us
Attached below is our logo and the color blue that we hope to use in the theme of the website
**** In the home page we want to focus on our partners and services****

Target Market(s)

Medical Sector

Industry/Entity Type

Medical

Coding

Coded - Design and coding required

Number of Pages Required

5+ page

Colors
0054AA
0677BA
7BADD7
CADEEF
E8F1F8

Requirements
Must have
• Animation in loading screen or animation in home page
Nice to have
• Some sort of animation for our partners

```html
<!DOCTYPE html>
<html lang="en">
<head>
<meta charset="utf-8">
<title>Zerovan Medical – Home</title>
<link rel="stylesheet" href="https://fonts.googleapis.com/css2?family=Ubuntu:wght@300;400;500;700&display=swap">
<style>
:root{
  --navy:#2a1b5c;
  --navy-2:#3a3f8f;
  --blue:#3f93d3;
  --blue-strong:#0677ba;
  --sky:#eaf3fb;
  --sky-2:#cadeef;
  --mist:#7badd7;
  --grey-text:#6b6b78;
  --ink:#1f1f2e;
  --white:#ffffff;
  --board:#000000;
}
*{box-sizing:border-box;margin:0;padding:0}
html,body{width:1200px;height:4035px;overflow:hidden;background:var(--board);font-family:'Ubuntu',sans-serif}
.canvas{position:relative;width:1200px;height:4035px;overflow:hidden}
.abs{position:absolute}

/* loading screen */
.splash{left:39px;top:78px;width:1121px;height:519px;
  background:radial-gradient(ellipse at 50% 45%,#ffffff 0%,#e3f1fa 45%,#a9d4ec 100%)}
.brand{display:flex;align-items:center;gap:14px;color:var(--navy);font-weight:500;white-space:nowrap}
.brand-mark{background:var(--blue);flex:none}
.splash .brand{position:absolute;left:50%;top:50%;transform:translate(-50%,-50%);font-size:62px}
.splash .brand-mark{width:62px;height:62px}

/* home page */
.page{left:39px;top:639px;width:1121px;height:3341px;background:var(--white);overflow:hidden}
.hero{left:0;top:0;width:1121px;height:469px;background:#ececee}
.hero-photo{left:462px;top:0;width:659px;height:469px;
  background:linear-gradient(120deg,#ececee 0%,#dfe8f5 25%,#b9cdf0 60%,#8fb0e6 100%)}
.hero-strip{left:462px;top:469px;width:659px;height:86px;background:#dbe9f7}
.sky-band{left:0;top:469px;width:1121px;height:1167px;background:var(--sky)}
.ghost{border:22px solid rgba(123,173,215,.18)}

.nav{left:93px;top:27px;display:flex;align-items:center}
.nav .brand{font-size:25px;gap:8px}
.nav .brand-mark{width:22px;height:22px}
.menu{left:332px;top:27px;height:25px;width:530px;font-size:13px;color:var(--ink)}
.menu a{color:inherit;text-decoration:none}
.menu .m{position:absolute;white-space:nowrap;top:0;line-height:25px}
.menu .active{background:var(--blue);color:var(--white);border-radius:13px;padding:0 14px}
.phone{left:874px;top:20px;display:flex;align-items:center;gap:8px;font-size:13px;color:var(--ink);white-space:nowrap}
.icon-circle{width:38px;height:38px;border-radius:50%;background:var(--white);border:3px solid var(--navy);display:flex;align-items:center;justify-content:center;flex:none}

.welcome{left:93px;top:122px;color:var(--blue);font-size:18px}
.hero-title{left:93px;top:150px;font-size:49px;line-height:60px;font-weight:500;color:var(--navy);white-space:nowrap}
.hero-title span{color:var(--blue);font-weight:400}
.hero-text{left:93px;top:275px;width:410px;font-size:13px;line-height:20px;color:var(--grey-text)}
.btn{display:flex;align-items:center;justify-content:center;color:var(--white);font-weight:500;
  background:linear-gradient(90deg,var(--navy),var(--navy-2));white-space:nowrap}
.btn-start{left:93px;top:353px;width:148px;height:45px;font-size:18px;border-radius:18px 4px 0 0}

.partners{left:93px;top:470px;width:935px;height:334px;background:var(--white)}
.partners .brand{position:absolute;left:50%;top:56px;transform:translate(-50%,-50%);font-size:44px}
.partners .brand-mark{width:44px;height:44px}
.sec-title{position:absolute;left:0;width:100%;text-align:center;color:var(--ink);font-size:26px;font-weight:400}
.partner-card{position:absolute;top:188px;width:190px;height:107px;background:var(--white);box-shadow:0 2px 8px rgba(0,0,0,.18);display:flex;align-items:center;justify-content:center}
.badge{width:110px;height:40px;border-radius:6px;background:#d7dce6}
.badge.round{width:56px;height:56px;border-radius:50%}

.svc-head{left:0;width:1121px;text-align:center}
.svc-kicker{top:905px;font-size:17px;color:var(--ink)}
.svc-title{top:928px;font-size:42px;color:var(--blue);font-weight:500}
.svc-card{position:absolute;top:1016px;width:300px;height:442px;overflow:hidden}
.svc-img{height:246px;background:linear-gradient(160deg,#e6f0fb,#7fb0e4 55%,#2f65b8)}
.svc-img.teal{background:linear-gradient(180deg,#cfeaf8,#6fb9e3 50%,#1d6aa6)}
.svc-body{background:var(--blue);height:196px;padding:14px 22px;color:var(--white)}
.svc-body h3,.svc-dark h3{font-size:28px;font-weight:500;margin-bottom:12px}
.svc-body p{font-size:13px;line-height:19px}
.more{display:inline-block;margin-top:16px;font-size:13px;font-weight:500;letter-spacing:.5px}
.svc-dark{background:linear-gradient(160deg,#4a4f8d,#2a2a66 70%,#23235a);color:var(--white);padding:80px 23px 0}
.svc-dark p{font-size:15px;line-height:26px}
.btn-all{left:459px;top:1494px;width:204px;height:47px;font-size:18px;border-radius:18px 4px 0 0}

.training{left:93px;top:1710px;width:935px;height:491px;background:var(--sky)}
.training .brand{position:absolute;left:50%;top:77px;transform:translate(-50%,-50%);font-size:44px}
.training .brand-mark{width:44px;height:44px}
.training p{position:absolute;left:50px;width:835px;top:190px;text-align:center;font-size:17px;line-height:28px;color:var(--grey-text);font-weight:300}
.btn-learn{left:366px;top:381px;width:204px;height:47px;font-size:18px;border-radius:18px 4px 0 0}

.about-kicker{left:93px;top:2280px;font-size:19px;color:var(--ink);font-weight:500}
.about-title{left:93px;top:2305px;font-size:45px;color:var(--blue);font-weight:500;white-space:nowrap}
.about-text{left:478px;top:2292px;width:515px;font-size:13px;line-height:20px;color:var(--grey-text)}
.member{position:absolute;top:2388px;width:299px;height:370px}
.member-photo{width:299px;height:300px;background:linear-gradient(180deg,#8c7e72,#3f3a3a)}
.member-photo.b{background:linear-gradient(180deg,#3a4660,#22283a)}
.member-photo.c{background:linear-gradient(180deg,#9aa4ab,#3b3634)}
.member-card{position:absolute;left:15px;top:259px;width:268px;height:108px;background:var(--white);box-shadow:0 2px 8px rgba(0,0,0,.14);text-align:center;padding-top:18px}
.member-card h4{font-size:20px;font-weight:500;color:var(--ink)}
.member-card span{display:block;margin-top:12px;font-size:17px;color:var(--grey-text)}

.footer{left:0;top:2868px;width:1121px;height:473px;background:var(--navy);color:var(--white)}
.footer .brand{position:absolute;left:50%;top:116px;transform:translate(-50%,-50%);font-size:56px;color:var(--white)}
.footer .brand-mark{width:54px;height:54px;background:var(--white)}
.foot-nav .f{position:absolute;top:214px;font-size:19px;transform:translateX(-50%);white-space:nowrap}
.contact{position:absolute;top:277px;display:flex;align-items:center;gap:10px;font-size:14px;line-height:20px;white-space:nowrap}
.contact .icon-circle{border:3px solid var(--blue);background:var(--white)}
.foot-line{position:absolute;left:96px;top:364px;width:931px;height:1px;background:rgba(255,255,255,.45)}
.copy{position:absolute;left:0;width:100%;top:400px;text-align:center;font-size:15px;font-weight:500}
</style>
</head>
<body>
<div class="canvas">

  <section class="abs splash" role="img" aria-label="Loading screen with soft blue molecular hexagon background">
    <div class="brand"><span class="brand-mark"></span>Zerovan Medical</div>
  </section>

  <main class="abs page">
    <div class="abs hero"></div>
    <div class="abs ghost" style="left:20px;top:90px;width:250px;height:380px"></div>
    <div class="abs hero-photo" role="img" aria-label="Photo of a CT scanner in a bright hospital room"></div>
    <div class="abs hero-strip"></div>
    <div class="abs sky-band"></div>
    <div class="abs ghost" style="left:20px;top:650px;width:260px;height:300px"></div>
    <div class="abs ghost" style="left:820px;top:1180px;width:301px;height:380px"></div>

    <header>
      <div class="abs nav"><div class="brand"><span class="brand-mark"></span>Zerovan</div></div>
      <nav class="abs menu">
        <a class="m active" style="left:0">Home</a>
        <a class="m" style="left:93px">Projects</a>
        <a class="m" style="left:185px">Services</a>
        <a class="m" style="left:279px">Training</a>
        <a class="m" style="left:372px">About</a>
        <a class="m" style="left:453px">Contact us</a>
      </nav>
      <div class="abs phone">
        <span class="icon-circle"><svg width="18" height="18" viewBox="0 0 24 24"><path fill="#3f93d3" d="M6.6 10.8a15 15 0 0 0 6.6 6.6l2.2-2.2a1 1 0 0 1 1-.25 11.4 11.4 0 0 0 3.6.57 1 1 0 0 1 1 1V20a1 1 0 0 1-1 1A17 17 0 0 1 3 4a1 1 0 0 1 1-1h3.5a1 1 0 0 1 1 1c0 1.25.2 2.45.57 3.57a1 1 0 0 1-.25 1z"/></svg></span>
        +964 770 123 4567
      </div>
    </header>

    <div class="abs welcome">Welcome to</div>
    <h1 class="abs hero-title">Zerovan <span>Medical</span><br><span>Appliances</span></h1>
    <p class="abs hero-text">Sed ut perspiciatis unde omnis iste natus error sit voluptatem accusantium doloremque laudantium, totam rem aperiam, eaque ipsa quae ab illo inventore</p>
    <a class="abs btn btn-start">Get Started</a>

    <section class="abs partners">
      <div class="brand"><span class="brand-mark"></span>Zerovan</div>
      <h2 class="sec-title" style="top:118px">Our Partners</h2>
      <div class="partner-card" style="left:37px"><span class="badge"></span></div>
      <div class="partner-card" style="left:260px"><span class="badge round"></span></div>
      <div class="partner-card" style="left:473px"><span class="badge"></span></div>
      <div class="partner-card" style="left:697px"><span class="badge round"></span></div>
    </section>

    <div class="abs svc-head svc-kicker">Our</div>
    <h2 class="abs svc-head svc-title">Services</h2>

    <article class="svc-card" style="left:93px">
      <div class="svc-img" role="img" aria-label="Photo of a modern operating theatre with imaging equipment"></div>
      <div class="svc-body"><h3>Support</h3><p>Lorem ipsum dolor sit amet, consectetur adipiscing elit, sed do eiusmod tempor incididunt ut labore et dolore magna aliqua.</p><span class="more">LEARN MORE &#187;</span></div>
    </article>
    <article class="svc-card svc-dark" style="left:409px" aria-label="Installation service over a photo of a scanner">
      <h3>Installation</h3>
      <p>Sed ut perspiciatis unde omnis iste natus error sit voluptatem accusantium doloremque laudantium, totam rem aperiam, eaque ipsa quae ab illo inventore veritatis et quasi architecto beatae vitae dicta sunt explicabo.</p>
      <span class="more" style="margin-top:20px;font-size:15px">LEARN MORE &#187;</span>
    </article>
    <article class="svc-card" style="left:726px">
      <div class="svc-img teal" role="img" aria-label="Photo of a futuristic imaging room with glowing ceiling"></div>
      <div class="svc-body"><h3>Training</h3><p>Lorem ipsum dolor sit amet, consectetur adipiscing elit, sed do eiusmod tempor incididunt ut labore et dolore magna aliqua.</p><span class="more">LEARN MORE &#187;</span></div>
    </article>
    <a class="abs btn btn-all">View All Services</a>

    <section class="abs training">
      <div class="brand"><span class="brand-mark"></span>Zerovan</div>
      <h2 class="sec-title" style="top:126px">Training</h2>
      <p>Sed ut perspiciatis unde omnis iste natus error sit voluptatem accusantium doloremque laudantium, totam rem aperiam, eaque ipsa quae ab illo inventore veritatis et quasi architecto beatae vitae dicta sunt explicabo. Nemo enim ipsam voluptatem quia voluptas sit aspernatur aut odit aut fugit, sed quia consequuntur magni dolores eos qui ratione voluptatem sequi nesciunt. Neque porro quisquam est, qui dolorem ipsum quia dolor sit amet, consectetur, adipisci velit, sed quia non numquam eius modi tempora incidunt ut labore et dolore magnam aliquam quaerat voluptatem.</p>
      <a class="abs btn btn-learn">Learn More</a>
    </section>

    <div class="abs about-kicker">About Us</div>
    <h2 class="abs about-title">Meet Our Team</h2>
    <p class="abs about-text">Sed ut perspiciatis unde omnis iste natus error sit voluptatem accusantium doloremque laudantium, totam rem aperiam, eaque ipsa quae ab illo inventore veritatis et quasi architecto beatae vitae</p>

    <div class="member" style="left:93px">
      <div class="member-photo" role="img" aria-label="Portrait photo of the chief medical officer"></div>
      <div class="member-card"><h4>Dr. Lina Haddad</h4><span>Chief Medical Officer</span></div>
    </div>
    <div class="member" style="left:411px">
      <div class="member-photo b" role="img" aria-label="Portrait photo of the chief executive officer"></div>
      <div class="member-card"><h4>Omar Sadeq</h4><span>Chief Executive Officer</span></div>
    </div>
    <div class="member" style="left:729px">
      <div class="member-photo c" role="img" aria-label="Portrait photo of the chief operating officer"></div>
      <div class="member-card"><h4>Noor Khalil</h4><span>Chief Operating Officer</span></div>
    </div>

    <footer class="abs footer">
      <div class="brand"><span class="brand-mark"></span>Zerovan</div>
      <nav class="foot-nav">
        <a class="f" style="left:234px">Home</a>
        <a class="f" style="left:354px">Projects</a>
        <a class="f" style="left:484px">Services</a>
        <a class="f" style="left:613px">Training</a>
        <a class="f" style="left:733px">About</a>
        <a class="f" style="left:865px">Contact us</a>
      </nav>
      <div class="contact" style="left:251px">
        <span class="icon-circle"><svg width="16" height="18" viewBox="0 0 24 24"><path fill="#3f93d3" d="M12 2a7 7 0 0 0-7 7c0 5 7 13 7 13s7-8 7-13a7 7 0 0 0-7-7zm0 9.5A2.5 2.5 0 1 1 12 6.5a2.5 2.5 0 0 1 0 5z"/></svg></span>
        <span>27 Karrada Street<br>Baghdad Iraq 10071</span>
      </div>
      <div class="contact" style="left:498px">
        <span class="icon-circle"><svg width="16" height="16" viewBox="0 0 24 24"><path fill="#3f93d3" d="M6.6 10.8a15 15 0 0 0 6.6 6.6l2.2-2.2a1 1 0 0 1 1-.25 11.4 11.4 0 0 0 3.6.57 1 1 0 0 1 1 1V20a1 1 0 0 1-1 1A17 17 0 0 1 3 4a1 1 0 0 1 1-1h3.5a1 1 0 0 1 1 1c0 1.25.2 2.45.57 3.57a1 1 0 0 1-.25 1z"/></svg></span>
        <span>+964 770 123 4567</span>
      </div>
      <div class="contact" style="left:699px">
        <span class="icon-circle"><svg width="16" height="14" viewBox="0 0 24 18"><path fill="#3f93d3" d="M2 0h20a2 2 0 0 1 2 2v14a2 2 0 0 1-2 2H2a2 2 0 0 1-2-2V2a2 2 0 0 1 2-2zm0 3v.5l10 6.5 10-6.5V3L12 9.3z"/></svg></span>
        <span>info@zerovanmedical.com</span>
      </div>
      <div class="foot-line"></div>
      <div class="copy">Copyright © 2024 Zerovan Medical . All Rights Reserved.</div>
    </footer>
  </main>
</div>
</body>
</html>
```